Morvela Aesthetic Doctor

I require an elegant, luxurious looking business card for my aesthetic business. I am a doctor and that will set me aside from competitors. I am planning to provide home and spa based treatments to clients with high expectations. I have attached my logo.

```html
<!DOCTYPE html>
<html lang="en">
<head>
<meta charset="utf-8">
<title>Morvela Aesthetic Doctor – Business Card</title>
<link rel="stylesheet" href="https://fonts.googleapis.com/css2?family=Open+Sans:wght@300;400;600&display=swap">
<style>
  :root {
    --stage: #d8d8d8;
    --card-light: #efefed;
    --card-blue: #c6dde8;
    --card-back: #e1eaee;
    --ink: #2a2a2a;
    --ink-soft: #3d3d3d;
    --accent: #4ea3d6;
    --accent-deep: #2f7fc0;
    --icon: #6aaed8;
  }
  * { box-sizing: border-box; margin: 0; padding: 0; }
  html, body { width: 1200px; height: 1129px; overflow: hidden; }
  body {
    background: var(--stage);
    font-family: "Open Sans", Arial, sans-serif;
    color: var(--ink);
    position: relative;
  }
  .card {
    position: absolute;
    left: 150px;
    width: 900px;
    height: 514px;
    box-shadow: 0 6px 18px rgba(0,0,0,0.15);
    overflow: hidden;
  }
  .card--front { top: 32px; display: flex; }
  .card--back { top: 583px; background: var(--card-back); }

  .front-details {
    width: 57%;
    background: var(--card-light);
    padding: 150px 0 0 70px;
  }
  .doctor-name {
    font-size: 30px;
    font-weight: 400;
    color: var(--ink);
    line-height: 1.1;
  }
  .doctor-name .postnominals { font-size: 15px; margin-left: 4px; }
  .doctor-diploma {
    font-size: 17px;
    font-variant: small-caps;
    color: var(--accent);
    letter-spacing: 0.5px;
    margin-top: 2px;
  }
  .contact-list { list-style: none; margin-top: 34px; margin-left: 26px; }
  .contact-list li {
    display: flex;
    align-items: center;
    height: 43px;
    font-size: 18px;
    color: var(--ink-soft);
    font-weight: 400;
  }
  .contact-list svg { width: 24px; height: 24px; margin-right: 28px; flex: none; }

  .front-services {
    width: 43%;
    background: var(--card-blue);
    padding: 64px 0 0 0;
    text-align: center;
  }
  .brand {
    display: flex;
    align-items: center;
    justify-content: center;
    gap: 12px;
    color: var(--accent-deep);
    font-weight: 400;
  }
  .brand-dot { border-radius: 50%; border: 2px solid var(--accent-deep); flex: none; }
  .brand--small .brand-name { font-size: 22px; letter-spacing: 1px; }
  .brand--small .brand-dot { width: 22px; height: 22px; }
  .service-list { list-style: none; margin-top: 40px; }
  .service-list li { font-size: 19px; color: var(--ink); line-height: 41px; }

  .back-wash {
    position: absolute;
    right: 0; top: 0;
    width: 62%; height: 100%;
    background: radial-gradient(ellipse at 85% 45%, rgba(78,163,214,0.45), rgba(160,205,230,0.25) 45%, rgba(225,234,238,0) 75%);
  }
  .back-content {
    position: absolute;
    left: 0; right: 0; top: 250px;
    text-align: center;
  }
  .brand--large .brand-name { font-size: 46px; letter-spacing: 2px; }
  .brand--large .brand-dot { width: 46px; height: 46px; }
  .back-web { margin-top: 30px; font-size: 34px; color: var(--ink); font-weight: 400; letter-spacing: 1px; }
</style>
</head>
<body>
  <section class="card card--front">
    <div class="front-details">
      <h1 class="doctor-name">Dr Liesel Varnholt<span class="postnominals">MRCPCH MD</span></h1>
      <p class="doctor-diploma">Australasian Diploma of Aesthetic Medicine</p>
      <ul class="contact-list">
        <li>
          <svg viewBox="0 0 24 24" fill="none" stroke="var(--icon)" stroke-width="1.4"><rect x="6" y="2" width="12" height="20" rx="2"/><line x1="10" y1="18.5" x2="14" y2="18.5"/></svg>
          0800 555 014
        </li>
        <li>
          <svg viewBox="0 0 24 24" fill="none" stroke="var(--icon)" stroke-width="1.4"><rect x="2" y="5" width="20" height="14" rx="1"/><polyline points="2,6 12,13 22,6"/></svg>
          liesel@morvela.co.nz
        </li>
        <li>
          <svg viewBox="0 0 24 24" fill="none" stroke="var(--icon)" stroke-width="1.4"><circle cx="12" cy="12" r="10"/><ellipse cx="12" cy="12" rx="4.5" ry="10"/><line x1="2" y1="12" x2="22" y2="12"/><path d="M4 7h16M4 17h16"/></svg>
          www.morvela.co.nz
        </li>
        <li>
          <svg viewBox="0 0 24 24" fill="none" stroke="var(--icon)" stroke-width="1.4"><rect x="4" y="4" width="16" height="16" rx="2"/></svg>
          dr_liesel_varnholt
        </li>
        <li>
          <svg viewBox="0 0 24 24" fill="none" stroke="var(--icon)" stroke-width="1.4"><circle cx="12" cy="12" r="9"/></svg>
          dr_liesel_varnholt
        </li>
      </ul>
    </div>
    <div class="front-services">
      <div class="brand brand--small">
        <span class="brand-dot"></span>
        <span class="brand-name">Morvela Aesthetic Doctor</span>
      </div>
      <ul class="service-list">
        <li>Dermal injectables</li>
        <li>Plasma facials</li>
        <li>Microneedling</li>
        <li>Skin boosters</li>
        <li>Excessive sweating</li>
      </ul>
    </div>
  </section>

  <section class="card card--back">
    <div class="back-wash" role="img" aria-label="Soft flowing blue brand decoration"></div>
    <div class="back-content">
      <div class="brand brand--large">
        <span class="brand-dot"></span>
        <span class="brand-name">Morvela Aesthetic Doctor</span>
      </div>
      <p class="back-web">www.morvela.co.nz</p>
    </div>
  </section>
</body>
</html>
```